Medical VIP club - small design

Please read the specs in a design brief attached. Also we don't have logo in a Vector format and attaching the only version we have.

Industry/Entity Type

Club

```html
<!DOCTYPE html>
<html lang="en">
<head>
<meta charset="utf-8">
<title>Veridan – V.I.P Club</title>
<link rel="stylesheet" href="https://fonts.googleapis.com/css2?family=Gelasio:ital,wght@0,400;0,600;0,700;1,400;1,600&display=swap">
<style>
:root{
  --topbar:#2b1c0b;
  --bg-center:#8a3615;
  --bg-edge:#3b130a;
  --tan:#e6d3a3;
  --tan-dark:#cbb27a;
  --gold:#d8bd83;
  --gold-soft:#c9a86a;
  --text-dark:#3a2a14;
  --panel-border:#c8ab7c;
  --panel-fill:#4a1a0d;
  --menu-bg:#2a241c;
  --menu-text:#b69f6c;
  --vip-bg:#0f0c09;
  --caption-bg:#8d7a55;
  --caption-text:#2e2412;
  --footer-bg:#3d0d08;
  --footer-text:#b99a72;
  --cream:#f2e6c8;
}
*{margin:0;padding:0;box-sizing:border-box}
html,body{width:1200px;height:1096px;overflow:hidden}
body{
  position:relative;
  font-family:"Gelasio",Georgia,serif;
  background:radial-gradient(ellipse 70% 60% at 50% 35%,var(--bg-center),var(--bg-edge));
}
.abs{position:absolute}
.top-bar{left:0;top:0;width:1200px;height:39px;background:var(--topbar);border-bottom:1px solid #55391a}
.top-bar a{position:absolute;top:10px;font-size:17px;color:var(--gold);text-decoration:none;font-style:italic;font-weight:600}
.top-bar .reg{left:877px}
.top-bar .sign{left:1002px;text-decoration:underline;font-weight:400}
.brand{left:115px;top:74px;display:flex;align-items:center;gap:10px}
.brand-dot{width:26px;height:26px;border-radius:50%;background:var(--gold-soft)}
.brand-name{font-size:40px;font-weight:600;color:var(--gold-soft);line-height:1}
.brand-sub{left:152px;top:122px;font-size:13px;color:var(--gold-soft);letter-spacing:1px}
.contact{left:941px;top:82px;height:52px;border-left:2px solid var(--gold-soft);padding-left:14px}
.contact h3{font-size:19px;font-weight:700;color:var(--gold-soft)}
.contact p{font-size:18px;color:var(--gold-soft)}
.panel{left:117px;top:158px;width:966px;height:819px;border:2px solid var(--panel-border);border-bottom:none;background:linear-gradient(#54200f,#3f160a);border-radius:3px 3px 0 0}
.nav{left:119px;top:160px;width:962px;height:31px;background:linear-gradient(#eedfb5,#d9c38e);border-bottom:1px solid #9c8455}
.nav span{position:absolute;top:6px;transform:translateX(-50%);font-size:16px;color:var(--text-dark);white-space:nowrap}
.nav .strong{font-weight:700}
.nav i{position:absolute;top:8px;width:1px;height:16px;background:var(--text-dark)}
.hero-photo{left:129px;top:213px;width:656px;height:387px;background:linear-gradient(135deg,#c9b79a,#e4d5b8 40%,#8d7456 75%,#5c4632)}
.vip{left:785px;top:213px;width:285px;height:387px;background:var(--vip-bg);color:var(--cream)}
.vip-title{position:absolute;left:28px;top:44px;font-size:66px;font-weight:700;color:#d6bc82;letter-spacing:2px;line-height:1}
.vip-club{position:absolute;left:42px;top:110px;font-size:52px;font-style:italic;color:#d6bc82;letter-spacing:4px;line-height:1}
.vip-lead{position:absolute;left:27px;top:195px;width:240px;font-size:19px;font-weight:700;line-height:1.2}
.vip-body{position:absolute;left:27px;top:260px;width:245px;font-size:14px;line-height:1.22}
.vip-more{position:absolute;right:20px;top:360px;font-size:15px;font-weight:700}
.menu{left:498px;top:196px;width:170px;height:253px;background:var(--menu-bg);border:1px solid #5a4a30;padding:10px 12px}
.menu li{list-style:none;height:39.5px;line-height:34px;border-bottom:2px dotted #8f7b55;font-size:17px;font-style:italic;font-weight:600;color:var(--menu-text);padding-left:12px}
.menu li:last-child{border-bottom:none}
.dots{left:819px;top:610px;display:flex;gap:7px;align-items:center}
.dots b{width:20px;height:20px;border:1px solid #8a6a4a;background:#4a1c0e}
.dots .on{width:26px;height:26px;background:#8d6a4a;border-color:#b08d66}
.tile{top:642px;height:184px;border:2px solid #a4906a}
.caption-bar{left:129px;top:826px;width:941px;height:51px;background:linear-gradient(#9d8a63,#7f6c48)}
.caption{position:absolute;top:0;height:51px;display:flex;align-items:center;justify-content:center;text-align:center;font-style:italic;font-size:16px;line-height:1.1;color:var(--caption-text)}
.caption-bar i{position:absolute;top:14px;width:1px;height:22px;background:#3a2e1a}
.follow{left:887px;top:946px;font-size:14px;color:var(--cream)}
.social{left:976px;top:935px;display:flex;gap:4px}
.social b{width:29px;height:29px;background:linear-gradient(#d9c59a,#a48d61);border:1px solid #6b5634;border-radius:3px}
.footer{left:0;top:976px;width:1200px;height:120px;background:linear-gradient(#4a0f09,#300805)}
.footer-links{position:absolute;left:125px;top:45px;font-size:15px;color:var(--footer-text)}
.footer-links strong{font-weight:700}
.copy{position:absolute;left:682px;top:45px;font-size:15px;color:var(--footer-text)}
.foot-brand{position:absolute;left:958px;top:36px;display:flex;align-items:center;gap:6px}
.foot-brand .brand-dot{width:14px;height:14px}
.foot-brand span{font-size:24px;font-weight:600;color:var(--gold-soft)}
</style>
</head>
<body>
<header class="abs top-bar">
  <a class="reg" href="#">Registration</a>
  <a class="sign" href="#">Sign In</a>
</header>

<div class="abs brand"><span class="brand-dot"></span><span class="brand-name">Veridan</span></div>
<div class="abs brand-sub">Medical Club</div>

<div class="abs contact"><h3>Contact Us</h3><p>01400-555-010</p></div>

<main class="abs panel"></main>

<nav class="abs nav">
  <span class="strong" style="left:46px">Home</span><i style="left:99px"></i>
  <span style="left:168px">About Us</span><i style="left:240px"></i>
  <span style="left:306px">V.I.P Club</span><i style="left:381px"></i>
  <span style="left:456px">Services</span><i style="left:534px"></i>
  <span style="left:658px">Packages and Prices</span><i style="left:774px"></i>
  <span class="strong" style="left:858px">Registration</span>
</nav>

<div class="abs hero-photo" role="img" aria-label="Photo of an elegant boutique interior with a crystal chandelier and glass display shelves"></div>

<section class="abs vip">
  <div class="vip-title">V.I.P</div>
  <div class="vip-club">CLUB</div>
  <p class="vip-lead">I am an ambitious, innovative and creative</p>
  <p class="vip-body">&nbsp;designer, who has an eye for detail, Art and design has been passion since my early years. I have taken a real interest and love for Typography, Photography and layout in various areas</p>
  <span class="vip-more">More</span>
</section>

<ul class="abs menu">
  <li>Option 1</li><li>Option 2</li><li>Option 3</li><li>Option 4</li><li>Option 5</li><li>Option 6</li>
</ul>

<div class="abs dots"><b></b><b></b><b class="on"></b><b></b><b></b><b></b><b></b><b></b></div>

<div class="abs tile" style="left:129px;width:185px;background:linear-gradient(135deg,#7a1010,#b3161a 60%,#3a0606)" role="img" aria-label="Photo of a red emergency direction sign with an arrow"></div>
<div class="abs tile" style="left:314px;width:186px;background:linear-gradient(160deg,#e0e0e0,#9a9a9a 60%,#505050)" role="img" aria-label="Black and white photo of a modern train at a station"></div>
<div class="abs tile" style="left:500px;width:184px;background:linear-gradient(150deg,#f0f0f0,#b0b0b0 50%,#606060)" role="img" aria-label="Black and white photo of doctors examining a patient"></div>
<div class="abs tile" style="left:684px;width:195px;background:linear-gradient(150deg,#c8c8c8,#8a8a8a 50%,#3e3e3e)" role="img" aria-label="Black and white photo of a hotel waiter serving at a table"></div>
<div class="abs tile" style="left:879px;width:191px;background:linear-gradient(#ffffff,#b8b8b8 55%,#606060)" role="img" aria-label="Black and white photo of a group of people standing together"></div>

<div class="abs caption-bar">
  <span class="caption" style="left:0;width:185px;font-size:17px;font-weight:600">Emergency<br>services</span><i style="left:184px"></i>
  <span class="caption" style="left:185px;width:186px">Transportation<br>services</span><i style="left:370px"></i>
  <span class="caption" style="left:371px;width:184px">Variety of Doctors</span><i style="left:554px"></i>
  <span class="caption" style="left:555px;width:195px;font-size:18px">Hotel Services</span><i style="left:749px"></i>
  <span class="caption" style="left:750px;width:191px">Become a Member</span>
</div>

<span class="abs follow">Follow us</span>
<div class="abs social"><b></b><b></b><b></b></div>

<footer class="abs footer">
  <div class="footer-links">Home | Vip Club | Services &nbsp;| &nbsp;Packages and Prices &nbsp;| <strong>Registration</strong></div>
  <div class="copy">© All Rights Reserved 2011 Veridan</div>
  <div class="foot-brand"><span class="brand-dot"></span><span>Veridan</span></div>
</footer>
</body>
</html>
```